Business Card for Multi-Brand Sportswear Company

We are looking for a business card which represents our company and the multiple brands within it.

The company: Kelt Athletic (LTD)
The brands: Kelt, PawaLuni, VerdantFlex, Grit and Gale

Employees using these cards would be representing Kelt Athletic, rather than any of the individual brands. You will see a current design within the uploaded files, to give some inspiration. The actual text of the brands is not necessary, but the logos should be on there is some format.

Our creative minds on this are stretched, so we are looking for someone to make this their own, and show us what a good business card should look like.

We may like to get these printed with spot gloss, so keep that in mind with your designs.

www.keltathletic.co.uk

Industry/Entity Type

Business

Contact Information for Business Card

Tom Hollingsworth-Pryce
Operations Manager
(+44) 1632 960 418
Tom@keltathletic.co.uk
www.keltathletic.co.uk

Font styles to use
Sans Serif
Other font styles liked:
• Eurostile

Colors
ffffff

Requirements
Nice to have
• Dark (black) background

```html
<!DOCTYPE html>
<html lang="en">
<head>
<meta charset="utf-8">
<title>Kelt Athletic – Business Card</title>
<link rel="stylesheet" href="https://fonts.googleapis.com/css2?family=Titillium+Web:wght@400;600;700&display=swap">
<style>
  :root {
    --stage: #2b2826;
    --card: #121212;
    --card-back: #161616;
    --white: #ffffff;
    --soft: #d9d9d9;
    --red: #e0222b;
    --gloss: #3a3a3a;
    --muted: #8a8a8a;
    --band: #4a4a4a;
  }
  * { box-sizing: border-box; margin: 0; padding: 0; }
  html, body { width: 1200px; height: 716px; overflow: hidden; }
  body {
    background: var(--stage);
    font-family: "Titillium Web", sans-serif;
    position: relative;
  }
  .card {
    position: absolute;
    width: 520px;
    height: 297px;
    border-radius: 3px;
    box-shadow: 0 14px 30px rgba(0,0,0,.45);
    overflow: hidden;
  }
  .card-front { left: 50px; top: 100px; background: var(--card); }
  .card-back  { left: 630px; top: 320px; background: var(--card-back); }

  .front-wordmark {
    position: absolute; left: 34px; top: 34px;
    color: var(--white); font-weight: 700; font-size: 38px;
    letter-spacing: 1px; line-height: 1;
  }
  .accent-band {
    position: absolute; left: 320px; top: 50px;
    width: 200px; height: 18px;
    background: var(--band);
  }

  .contact { position: absolute; left: 34px; top: 108px; color: var(--soft); }
  .contact-name { color: var(--red); font-weight: 700; font-size: 20px; line-height: 1.1; }
  .contact-role { font-size: 14px; margin-bottom: 8px; }
  .contact-line { display: flex; align-items: center; gap: 8px; font-size: 14px; line-height: 1.45; }
  .contact-line svg { width: 11px; height: 11px; flex: none; }

  .brand-row {
    position: absolute; right: 26px; bottom: 24px;
    display: flex; gap: 18px; align-items: center;
  }
  .brand { display: flex; align-items: center; gap: 5px; color: var(--soft); font-size: 12px; font-weight: 600; }
  .brand-dot { width: 9px; height: 9px; border-radius: 50%; background: var(--red); }
  .brand-square { width: 9px; height: 9px; background: var(--muted); }

  .back-wordmark {
    position: absolute; left: 0; right: 0; top: 118px; text-align: center;
    color: var(--gloss); font-weight: 700; font-size: 46px; letter-spacing: 1px; line-height: 1;
  }
</style>
</head>
<body>
  <section class="card card-front">
    <div class="front-wordmark">Kelt Athletic</div>
    <div class="accent-band" role="img" aria-label="Decorative accent band running to the card edge"></div>

    <div class="contact">
      <p class="contact-name">Tom Hollingsworth-Pryce</p>
      <p class="contact-role">Operations Manager</p>
      <p class="contact-line">
        <svg viewBox="0 0 12 12" aria-hidden="true"><path fill="var(--red)" d="M2.5 1l2 2-1 1.5c.6 1.4 1.6 2.4 3 3l1.5-1 2 2-1.5 1.5C5 10 2 7 1 2.5z"/></svg>
        (+44) 1632 960 418
      </p>
      <p class="contact-line">
        <svg viewBox="0 0 12 12" aria-hidden="true"><rect x="1" y="2.5" width="10" height="7" fill="var(--red)"/><path d="M1 2.5l5 4 5-4" stroke="var(--card)" fill="none"/></svg>
        Tom@keltathletic.co.uk
      </p>
      <p class="contact-line">
        <svg viewBox="0 0 12 12" aria-hidden="true"><circle cx="6" cy="6" r="5" fill="var(--red)"/><path d="M1 6h10M6 1c-2.5 3-2.5 7 0 10M6 1c2.5 3 2.5 7 0 10" stroke="var(--card)" stroke-width=".8" fill="none"/></svg>
        www.keltathletic.co.uk
      </p>
    </div>

    <div class="brand-row">
      <span class="brand"><span class="brand-square"></span>PawaLuni</span>
      <span class="brand"><span class="brand-dot"></span>Grit and Gale</span>
      <span class="brand">Kelt</span>
      <span class="brand"><span class="brand-square"></span>VerdantFlex</span>
    </div>
  </section>

  <section class="card card-back">
    <div class="back-wordmark">Kelt Athletic</div>
  </section>
</body>
</html>
```